Email Banner (LumenBriefs)

We require an email banner for our email promotions sent to prospect clients. The banner needs to contain the wording LumenBriefs and use the same colour scheme as the logos attached.

This is for B2B professional's so needs to look like a place you would come to read technology articles.

```html
<!DOCTYPE html>
<html lang="en">
<head>
<meta charset="utf-8">
<title>LumenBriefs Email Banners</title>
<link href="https://fonts.googleapis.com/css2?family=Quicksand:wght@600&display=swap" rel="stylesheet">
<style>
  :root {
    --page: #ffffff;
    --wordmark: #ffffff;
    --trim-light: rgba(255, 255, 255, 0.55);
    --trim-fade: rgba(255, 255, 255, 0);
    --blue-core: #0091d2;
    --blue-mid: #04588a;
    --blue-edge: #03162c;
    --green-core: #82be42;
    --green-mid: #55883a;
    --green-edge: #1f3628;
  }
  * { margin: 0; padding: 0; box-sizing: border-box; }
  html, body {
    width: 1200px;
    height: 611px;
    overflow: hidden;
    background: var(--page);
  }
  .canvas {
    position: relative;
    width: 1200px;
    height: 611px;
  }
  .banner {
    position: absolute;
    left: 51px;
    width: 1106px;
    height: 231px;
    overflow: hidden;
  }
  .banner--blue {
    top: 66px;
    background: radial-gradient(ellipse 560px 300px at 554px 80px,
      var(--blue-core) 0%, var(--blue-mid) 55%, var(--blue-edge) 100%);
  }
  .banner--green {
    top: 318px;
    background: radial-gradient(ellipse 560px 300px at 554px 80px,
      var(--green-core) 0%, var(--green-mid) 55%, var(--green-edge) 100%);
  }
  .banner__trim {
    position: absolute;
    left: 0;
    top: 0;
    width: 100%;
    height: 49px;
    background: linear-gradient(to bottom, var(--trim-light) 0%, var(--trim-fade) 100%);
  }
  .banner__floor {
    position: absolute;
    inset: 0;
    width: 100%;
    height: 100%;
  }
  .banner__wordmark {
    position: absolute;
    left: 0;
    right: 0;
    top: 92px;
    padding-left: 38px;
    text-align: center;
    font-family: "Quicksand", sans-serif;
    font-weight: 600;
    font-size: 44px;
    line-height: 1;
    letter-spacing: 0.2px;
    color: var(--wordmark);
  }
</style>
</head>
<body>
<main class="canvas">

  <section class="banner banner--blue">
    <div class="banner__trim" role="img" aria-label="Decorative white striped border along the top edge"></div>
    <svg class="banner__floor" viewBox="0 0 1106 231" aria-hidden="true">
      <defs>
        <linearGradient id="band-upper-blue" x1="0" y1="0" x2="0" y2="1">
          <stop offset="0" stop-color="#000a1c" stop-opacity="0.75"/>
          <stop offset="1" stop-color="#000a1c" stop-opacity="0.15"/>
        </linearGradient>
        <linearGradient id="band-lower-blue" x1="0" y1="0" x2="0" y2="1">
          <stop offset="0" stop-color="#000a1c" stop-opacity="0.1"/>
          <stop offset="1" stop-color="#000a1c" stop-opacity="0.9"/>
        </linearGradient>
      </defs>
      <path d="M0 174 Q553 202 1106 174 L1106 206 L0 206 Z" fill="url(#band-upper-blue)"/>
      <rect x="0" y="206" width="1106" height="25" fill="url(#band-lower-blue)"/>
    </svg>
    <p class="banner__wordmark">LumenBriefs.io</p>
  </section>

  <section class="banner banner--green">
    <div class="banner__trim" role="img" aria-label="Decorative white striped border along the top edge"></div>
    <svg class="banner__floor" viewBox="0 0 1106 231" aria-hidden="true">
      <defs>
        <linearGradient id="band-upper-green" x1="0" y1="0" x2="0" y2="1">
          <stop offset="0" stop-color="#041018" stop-opacity="0.75"/>
          <stop offset="1" stop-color="#041018" stop-opacity="0.15"/>
        </linearGradient>
        <linearGradient id="band-lower-green" x1="0" y1="0" x2="0" y2="1">
          <stop offset="0" stop-color="#041018" stop-opacity="0.1"/>
          <stop offset="1" stop-color="#021020" stop-opacity="0.95"/>
        </linearGradient>
      </defs>
      <path d="M0 174 Q553 202 1106 174 L1106 206 L0 206 Z" fill="url(#band-upper-green)"/>
      <rect x="0" y="206" width="1106" height="25" fill="url(#band-lower-green)"/>
    </svg>
    <p class="banner__wordmark">LumenBriefs.io</p>
  </section>

</main>
</body>
</html>
```